Divorce Lawyer print and ebook cover (Lanterns over the quiet harbor )

I need a front and back cover for my divorce and family law book. I already have a photo and title. The back cover photo is not necessary but can be interesting the Front-main cover is a must

Target Market(s)

Prospective client

Colors

Designer to choose colors to be used in the design.

Requirements
Must have
• Front photo by viewable.

```html
<!DOCTYPE html>
<html lang="en">
<head>
<meta charset="utf-8">
<title>Divorce and Family Law Book – Cover Set</title>
<link rel="stylesheet" href="https://fonts.googleapis.com/css2?family=Cinzel:wght@400&family=Roboto+Mono:wght@400&family=Montserrat:wght@500&display=swap">
<style>
  :root {
    --backdrop: #d3d6da;
    --fog-light: #e6edf0;
    --fog-blue: #9fb4bd;
    --forest-gold: #d9bb5a;
    --leaf-green: #9fbf5e;
    --road-dark: #2c3236;
    --road-mid: #5a5c55;
    --cover-white: #f4f4f2;
    --board-grey: #4a4b4d;
    --gold-panel: #c9a92d;
    --gold-deep: #b39222;
    --ink: #2a2414;
  }
  * { margin: 0; padding: 0; box-sizing: border-box; }
  html, body { width: 1200px; height: 900px; overflow: hidden; }
  body {
    background: var(--backdrop);
    position: relative;
  }
  .cover {
    position: absolute;
    top: 150px;
    width: 420px;
    height: 600px;
  }
  /* Front cover */
  .front-cover { left: 150px; overflow: hidden; }
  .front-photo {
    position: absolute;
    inset: 0;
    background:
      radial-gradient(ellipse 70% 45% at 78% 28%, rgba(159,191,94,0.75), rgba(217,187,90,0) 70%),
      radial-gradient(ellipse 60% 40% at 25% 20%, rgba(230,237,240,0.95), rgba(230,237,240,0) 75%),
      linear-gradient(180deg, var(--fog-light) 0%, var(--fog-blue) 40%, var(--road-mid) 68%, var(--road-dark) 100%);
  }
  .front-titles {
    position: absolute;
    left: 0;
    right: 0;
    bottom: 90px;
    text-align: center;
    color: var(--cover-white);
    font-family: "Cinzel", serif;
  }
  .front-kicker {
    font-size: 8px;
    letter-spacing: 2.2px;
    text-transform: uppercase;
    margin-bottom: 14px;
  }
  .front-author {
    font-size: 22px;
    letter-spacing: 6px;
    text-transform: uppercase;
  }
  /* Back cover */
  .back-cover {
    left: 630px;
    background: var(--board-grey);
    padding: 18px;
  }
  .back-panel {
    position: relative;
    width: 100%;
    height: 100%;
    background: linear-gradient(160deg, var(--gold-panel) 0%, var(--gold-panel) 55%, var(--gold-deep) 100%);
  }
  .back-blurb {
    position: absolute;
    top: 150px;
    right: 50px;
    width: 140px;
    font-family: "Roboto Mono", monospace;
    color: var(--ink);
  }
  .back-blurb-heading {
    font-size: 7px;
    letter-spacing: 3.4px;
    margin-bottom: 8px;
    font-weight: 400;
  }
  .back-blurb-body {
    font-size: 7px;
    line-height: 1.45;
    letter-spacing: 0.6px;
    text-align: justify;
  }
  .back-imprint {
    position: absolute;
    left: 150px;
    bottom: 72px;
    font-family: "Montserrat", sans-serif;
    font-weight: 500;
    font-size: 14px;
    letter-spacing: 5px;
    color: var(--ink);
  }
</style>
</head>
<body>
  <section class="cover front-cover">
    <div class="front-photo" role="img" aria-label="Photograph of a man in a dark suit seen from behind at a fork in a misty road, with a grey 'Old Life' sign pointing left and a yellow 'New Life' sign pointing right, foggy bare trees on the left and sunlit green trees on the right"></div>
    <div class="front-titles">
      <p class="front-kicker">Divorce and Family Law Book</p>
      <p class="front-author">Marlow Whitcombe</p>
    </div>
  </section>

  <section class="cover back-cover">
    <div class="back-panel">
      <div class="back-blurb">
        <h2 class="back-blurb-heading">Book Cover Design Brief</h2>
        <p class="back-blurb-body">A calm, practical guide for anyone facing the end of a marriage. Step by step, it explains custody, support, property and the court process in plain language, so readers can make steady decisions, protect their children and begin again with confidence. Written by a family lawyer who has walked hundreds of clients through the same road toward a new life.</p>
      </div>
      <p class="back-imprint">LOGO</p>
    </div>
  </section>
</body>
</html>
```